Bref créative
Business Cards & Satationary for Copperfield Homes
Dallin Marsh
Professional
Copperfield Homes
PO Box 587
KELMORE RISE Q 4390
M: 0417 562 908
info@copperfieldhomes.com.au
www.copperfieldhomes.com.au
NHRA Licence No. 80394. Housing Registry Office of Tasmania No. HR-K61402
Residential Construction
"Builder of Quality not Quantity"
E:info@copperfieldhomes.com.au

```html
<!DOCTYPE html>
<html lang="en">
<head>
<meta charset="utf-8">
<title>Copperfield Homes — Stationery Concepts</title>
<link href="https://fonts.googleapis.com/css2?family=Montserrat:wght@400;600&display=swap" rel="stylesheet">
<style>
  :root{
    --stage:#3b2b23;
    --paper:#ffffff;
    --brand:#d1492a;
    --brand-dark:#a8341b;
    --grey:#8c8c8c;
    --grey-light:#c9c9c9;
    --ink:#555555;
    --label:#d8cfc8;
  }
  *{box-sizing:border-box;margin:0;padding:0}
  html,body{width:1200px;height:466px;overflow:hidden}
  body{background:var(--stage);font-family:"Montserrat",sans-serif;position:relative}
  .piece{position:absolute;background:var(--paper);overflow:hidden;box-shadow:0 3px 8px rgba(0,0,0,.45)}
  .piece svg.swoosh{position:absolute;left:0;width:100%}
  .label{position:absolute;font-size:6px;letter-spacing:1.5px;text-transform:uppercase;color:var(--label);text-align:center}
  .section-title{position:absolute;left:25px;top:128px;font-size:6px;letter-spacing:1.5px;text-transform:uppercase;color:var(--label)}
  .brand{display:flex;align-items:center;gap:3px;color:var(--brand);font-weight:600;white-space:nowrap}
  .brand .mark{background:var(--brand);flex:none}
  .contact{color:var(--ink);font-size:3.6px;line-height:5px}

  /* business cards */
  .card-front{left:25px;top:148px;width:110px;height:63px}
  .card-front .brand{position:absolute;left:8px;top:10px;font-size:6px}
  .card-front .brand .mark{width:8px;height:8px}
  .card-front .contact{position:absolute;right:6px;top:30px;text-align:right;font-size:3.4px;line-height:4.6px}
  .card-back{left:25px;top:240px;width:110px;height:63px;background:var(--brand)}
  .card-back .brand{position:absolute;left:50%;top:50%;transform:translate(-50%,-50%);color:var(--paper);font-size:7px}
  .card-back .brand .mark{background:var(--paper);width:9px;height:9px}

  /* letterheads */
  .letterhead{top:22px;width:250px;height:356px}
  .lh-one{left:205px}
  .lh-two{left:475px}
  .lh-one .brand{position:absolute;left:16px;top:16px;font-size:8px}
  .lh-one .brand .mark{width:11px;height:11px}
  .lh-one .contact{position:absolute;right:16px;top:14px;text-align:left}
  .lh-two .brand{position:absolute;left:50%;top:26px;transform:translateX(-50%);font-size:8px}
  .lh-two .brand .mark{width:11px;height:11px}
  .lh-two .faint-mark{position:absolute;left:50%;top:150px;width:56px;height:56px;transform:translateX(-50%);background:var(--brand);opacity:.12}
  .lh-two .footer{position:absolute;left:0;right:0;bottom:32px;text-align:center;font-size:3.4px}
  .lh-two .footer .accent{color:var(--brand)}

  /* envelopes */
  .envelope{left:780px;width:225px;height:102px}
  .env-open{top:22px;background:var(--brand)}
  .env-open .brand{position:absolute;left:50%;top:60px;transform:translateX(-50%);color:var(--paper);font-size:6px}
  .env-open .brand .mark{background:var(--paper);width:9px;height:9px}
  .env-grey{top:100px}
  .env-flap{top:175px}
  .env-front{top:300px}
  .env-front .brand{position:absolute;left:10px;top:10px;font-size:6px}
  .env-front .brand .mark{width:9px;height:9px}
  .env-front .contact{position:absolute;left:10px;top:24px;font-size:3px;line-height:4px}
  .envelope svg{position:absolute;inset:0;width:100%;height:100%}
</style>
</head>
<body>

  <div class="section-title">Stationery Concepts</div>

  <!-- Business card front -->
  <section class="piece card-front">
    <svg class="swoosh" style="bottom:0;height:16px" viewBox="0 0 110 16" preserveAspectRatio="none">
      <path d="M0 8 Q55 -2 110 6 L110 16 L0 16Z" fill="var(--grey-light)"/>
      <path d="M0 11 Q55 3 110 10 L110 16 L0 16Z" fill="var(--brand)"/>
    </svg>
    <div class="brand"><span class="mark"></span>Copperfield Homes</div>
    <div class="contact">
      Dallin Marsh<br>M: 0417 562 908<br>info@copperfieldhomes.com.au<br>www.copperfieldhomes.com.au
    </div>
  </section>
  <div class="label" style="left:25px;top:216px;width:110px">Business Card Front</div>

  <!-- Business card back -->
  <section class="piece card-back">
    <div class="brand"><span class="mark"></span>Copperfield Homes</div>
  </section>
  <div class="label" style="left:25px;top:308px;width:110px">Business Card Back</div>

  <!-- Letterhead option 1 -->
  <section class="piece letterhead lh-one">
    <svg class="swoosh" style="top:0;height:46px" viewBox="0 0 250 46" preserveAspectRatio="none">
      <path d="M0 0 L250 0 L250 6 Q130 2 0 30Z" fill="var(--brand)"/>
    </svg>
    <div class="brand"><span class="mark"></span>Copperfield Homes</div>
    <div class="contact">
      PO Box 587<br>KELMORE RISE Q 4390<br>M: 0417 562 908<br>E: info@copperfieldhomes.com.au
    </div>
    <svg class="swoosh" style="bottom:0;height:60px" viewBox="0 0 250 60" preserveAspectRatio="none">
      <path d="M0 18 Q120 52 250 20 L250 60 L0 60Z" fill="var(--grey)"/>
      <path d="M0 34 Q130 62 250 34 L250 60 L0 60Z" fill="var(--brand)"/>
    </svg>
  </section>
  <div class="label" style="left:205px;top:388px;width:250px">Letterhead Option 1</div>

  <!-- Letterhead option 2 -->
  <section class="piece letterhead lh-two">
    <svg class="swoosh" style="top:0;height:70px" viewBox="0 0 250 70" preserveAspectRatio="none">
      <path d="M250 0 L250 60 Q200 10 100 0Z" fill="var(--grey-light)"/>
      <path d="M250 0 L250 36 Q215 6 160 0Z" fill="var(--grey)"/>
    </svg>
    <div class="brand"><span class="mark"></span>Copperfield Homes</div>
    <div class="faint-mark"></div>
    <div class="contact footer">
      PO Box 587 <span class="accent">|</span> KELMORE RISE Q 4390 <span class="accent">|</span> M: 0417 562 908<br>
      info@copperfieldhomes.com.au <span class="accent">|</span> www.copperfieldhomes.com.au
    </div>
    <svg class="swoosh" style="bottom:0;height:26px" viewBox="0 0 250 26" preserveAspectRatio="none">
      <path d="M0 12 Q125 0 250 12 L250 26 L0 26Z" fill="var(--brand)"/>
    </svg>
  </section>
  <div class="label" style="left:475px;top:388px;width:250px">Letterhead Option 2</div>

  <!-- Envelopes -->
  <section class="piece envelope env-open">
    <svg viewBox="0 0 225 102" preserveAspectRatio="none">
      <path d="M0 0 L112 42 L225 0Z" fill="var(--brand-dark)"/>
    </svg>
    <div class="brand"><span class="mark"></span>Copperfield Homes</div>
  </section>

  <section class="piece envelope env-grey">
    <svg viewBox="0 0 225 102" preserveAspectRatio="none">
      <path d="M0 0 L112 44 L225 0Z" fill="var(--grey)"/>
      <path d="M0 0 L112 38 L225 0Z" fill="#6f6f6f"/>
    </svg>
  </section>

  <section class="piece envelope env-flap">
    <svg viewBox="0 0 225 102" preserveAspectRatio="none">
      <path d="M0 0 L112 46 L225 0" fill="none" stroke="var(--grey-light)" stroke-width="1"/>
    </svg>
  </section>

  <section class="piece envelope env-front">
    <svg viewBox="0 0 225 102" preserveAspectRatio="none">
      <path d="M0 86 Q112 74 225 84 L225 102 L0 102Z" fill="var(--brand)"/>
      <path d="M0 84 Q112 72 225 82 L225 84 Q112 74 0 86Z" fill="var(--grey)"/>
    </svg>
    <div class="brand"><span class="mark"></span>Copperfield Homes</div>
    <div class="contact">PO Box 587<br>KELMORE RISE Q 4390</div>
  </section>
  <div class="label" style="left:780px;top:410px;width:225px">Business Envelope</div>

</body>
</html>
```